Wix web design for healthcare IT consulting firm.

I am looking for a web design built in Wix that it will be easy for me to add or edit content in the future. The web site does not need to be overly complicated, but it should look very polished and professional. I also want to ensure it is mobile device friendly. I do not need any type of on-line purchasing ability. I will eventually do blogs, but for now it is a fairly standard web site with main page, about us, services provided, etc. I would also like a place for potential customers to contact us directly from the web site. I have included a Word document with some content for the web design. I have also included my logo and business card for reference. I would like to utilize similar colors as my business card. One of my primary competitors is https://vonmarlhq.example/

Target Market(s)

Target market could be nursing home CEO, CIO, or other leader at an organization that manages long term care facilities.

Number of Pages Required

5+ page

Colors
876aae

Requirements
Must have
• Be designed to be used in Wix. Use the content I provided to create and make web design. Allow to be viewed on mobile device. Please use similar color structure as attached business card. Please use attached logo in design.

```html
<!DOCTYPE html>
<html lang="en">
<head>
<meta charset="utf-8">
<title>Carewell Healthcare Solutions</title>
<link href="https://fonts.googleapis.com/css2?family=Raleway:wght@300;400;500;600;700&family=Open+Sans:wght@400;600;700&display=swap" rel="stylesheet">
<style>
:root{
  --purple:#876aae;
  --purple-deep:#6f4fa3;
  --ink:#222222;
  --body:#555555;
  --line:#d9d2e4;
  --white:#ffffff;
  --footer:#ebe7f2;
}
*{margin:0;padding:0;box-sizing:border-box}
html,body{width:1200px;height:3072px;overflow:hidden;background:var(--white)}
body{position:relative;font-family:"Open Sans",sans-serif;color:var(--body)}
.abs{position:absolute}
.brand{left:110px;top:18px;width:96px;height:96px;background:var(--purple-deep);display:flex;align-items:center;justify-content:center;color:var(--white);font-size:14px;font-weight:600}
.nav{top:50px;left:460px;display:flex;font-size:16px;color:#444}
.nav a{color:#444;text-decoration:none;margin-right:38px}
.nav a.active{color:var(--purple)}
.login{left:978px;top:46px;width:110px;height:38px;border-radius:19px;background:var(--purple);color:var(--white);font-size:15px;display:flex;align-items:center;justify-content:center;gap:8px;box-shadow:0 2px 4px rgba(0,0,0,.25)}
.hero{left:110px;top:130px;width:978px;height:475px;background:linear-gradient(120deg,#e4e7ee 0%,#c7cbd4 35%,#9fa6b3 60%,#dfe2e8 100%)}
.hero-title{left:110px;top:218px;width:978px;text-align:center;font-family:"Raleway",sans-serif;font-weight:300;font-size:60px;line-height:70px;color:var(--white)}
.hero-rule{left:594px;top:410px;width:1px;height:128px;background:rgba(255,255,255,.8)}
.hero-dot{left:590px;top:538px;width:9px;height:9px;border-radius:50%;background:var(--white)}
.hero-sub{left:110px;top:556px;width:978px;text-align:center;font-size:15px;color:var(--white)}
.social{left:38px;width:40px;height:40px;border-radius:50%;border:1.5px solid #999}
.ceo-name{left:122px;top:708px;font-size:15px;color:var(--ink)}
.ceo-role{left:122px;top:736px;font-family:"Raleway",sans-serif;font-weight:600;font-size:32px;color:var(--ink)}
.ceo-rule{left:122px;top:786px;width:98px;height:3px;background:var(--ink)}
.ceo-photo{left:145px;top:826px;width:184px;height:184px;border-radius:50%;border:3px solid #eee;background:radial-gradient(circle at 50% 40%,#e8d9b8,#b9bfd0)}
.ceo-text{left:606px;top:720px;width:470px;font-size:13.5px;line-height:31px}
.ceo-text p{margin-bottom:10px}
.btn-outline{border:2px solid var(--purple);color:var(--purple);border-radius:24px;display:flex;align-items:center;justify-content:center;font-size:15px;font-weight:600}
.btn-light{border:2px solid var(--white);color:var(--white);border-radius:26px;display:flex;align-items:center;justify-content:center;font-size:16px;font-weight:600}
.banner{left:0;top:1110px;width:1200px;height:423px;background:linear-gradient(120deg,#9b84bf,#876aae 55%,#a08bc3)}
.banner-title{left:0;top:1222px;width:1200px;text-align:center;font-family:"Raleway",sans-serif;font-weight:600;font-size:30px;line-height:52px;color:var(--white)}
.services-title{left:0;top:1628px;width:1200px;text-align:center;font-family:"Raleway",sans-serif;font-weight:600;font-size:32px;color:var(--ink)}
.services-rule{left:550px;top:1680px;width:100px;height:3px;background:var(--ink)}
.services-divider{left:600px;top:1752px;width:1px;height:360px;background:var(--line)}
.svc-icon{width:112px;height:112px;border-radius:50%;border:2.5px solid #333}
.svc-name{width:360px;text-align:center;font-weight:700;font-size:15px;line-height:24px;color:var(--ink)}
.svc-text{width:360px;text-align:center;font-size:13.5px;line-height:31px}
.contact{left:0;top:2211px;width:1200px;height:367px;background:var(--purple)}
.contact-title{left:155px;top:2266px;font-family:"Raleway",sans-serif;font-weight:700;font-size:26px;color:var(--white)}
.hours-label{left:155px;top:2333px;font-family:"Raleway",sans-serif;font-weight:600;font-size:17px;color:var(--white)}
.hours-rule{left:295px;top:2345px;width:98px;height:1px;background:rgba(255,255,255,.8)}
.hours{left:405px;top:2320px;font-size:13.5px;line-height:26px;color:var(--white)}
.hours span{display:inline-block;width:120px}
.c-icon{width:34px;height:34px;border-radius:50%;border:1.5px solid var(--white);display:flex;align-items:center;justify-content:center}
.c-text{font-size:13.5px;line-height:26px;color:var(--white)}
.c-divider{left:414px;top:2398px;width:1px;height:96px;background:rgba(255,255,255,.6)}
.field{height:32px;border:1px solid rgba(255,255,255,.6);background:rgba(255,255,255,.18);color:var(--white);font-size:12px;padding:0 10px;display:flex;align-items:center}
.field.area{align-items:flex-start;padding-top:8px}
.send{left:815px;top:2459px;width:124px;height:40px;border:2px solid var(--white);border-radius:20px;color:var(--white);font-size:16px;font-weight:600;display:flex;align-items:center;justify-content:center}
.map{left:0;top:2578px;width:1200px;height:424px;background:linear-gradient(135deg,#eef0ee,#e3e8e3 50%,#ecefe9)}
.map-btn{left:112px;top:2624px;width:116px;height:30px;background:var(--white);border:1px solid #888;font-size:12px;color:#333;display:flex;align-items:center;justify-content:center}
.footer{left:0;top:3002px;width:1200px;height:70px;background:var(--footer);display:flex;align-items:center;justify-content:center;font-size:13.5px;color:#444}
</style>
</head>
<body>

<header>
  <div class="abs brand">Carewell</div>
  <nav class="abs nav">
    <a class="active" href="#">Home</a><a href="#">About Us</a><a href="#">Services</a><a href="#">Our CEO</a><a href="#">Contact Us</a>
  </nav>
  <div class="abs login">
    <svg width="14" height="14" viewBox="0 0 14 14"><circle cx="7" cy="4" r="3.2" fill="#fff"/><path d="M1 14c0-4 2.7-6 6-6s6 2 6 6z" fill="#fff"/></svg>Login
  </div>
</header>

<section>
  <div class="abs hero" role="img" aria-label="Doctor writing on a clipboard at a desk with a stethoscope"></div>
  <h1 class="abs hero-title">CAREWELL HEALTHCARE<br>SOLUTIONS</h1>
  <div class="abs hero-rule"></div>
  <div class="abs hero-dot"></div>
  <p class="abs hero-sub">Increasing the value and security of your technology resources.</p>
  <div class="abs social" style="top:293px"></div>
  <div class="abs social" style="top:347px"></div>
  <div class="abs social" style="top:402px"></div>
</section>

<section>
  <p class="abs ceo-name">Dana Whitfield</p>
  <h2 class="abs ceo-role">PRESIDENT AND CEO</h2>
  <div class="abs ceo-rule"></div>
  <div class="abs ceo-photo" role="img" aria-label="Portrait of the company president"></div>
  <div class="abs ceo-text">
    <p>Sed ut perspiciatis unde omnis iste natus error sit voluptatem accusan tium do loremque laudantium, totam rem aperiam, eaque ipsa quae ab illo inventore veritatis et quasi architecto beatae vitae dicta sunt explicabo. fugit, sed quia con sequuntur magni dolores eosui ratione .</p>
    <p>Quasi architecto beatae vitae dicta sunt explicabo. Nemo enim ipsam votel uptatem quia voluptas sit aspernatur aut odit aut fugit, sed quia con sequa untur magni dolores eosui ratione .</p>
  </div>
  <div class="abs btn-outline" style="left:606px;top:966px;width:126px;height:44px">Read More</div>
</section>

<section>
  <div class="abs banner" role="img" aria-label="Soft purple-tinted photo of medical vials and equipment"></div>
  <h2 class="abs banner-title">INCREASING THE VALUE AND SECURITY OF YOUR<br>TECHNOLOGY RESOURCES</h2>
  <div class="abs btn-light" style="left:512px;top:1355px;width:176px;height:50px">View Our Blog</div>
</section>

<section>
  <h2 class="abs services-title">SERVICES</h2>
  <div class="abs services-rule"></div>
  <div class="abs services-divider"></div>

  <div class="abs svc-icon" style="left:300px;top:1739px">
    <svg width="107" height="107" viewBox="0 0 112 112"><rect x="38" y="28" width="34" height="54" rx="4" fill="none" stroke="#333" stroke-width="3"/><line x1="38" y1="38" x2="72" y2="38" stroke="#333" stroke-width="2"/><line x1="38" y1="72" x2="72" y2="72" stroke="#333" stroke-width="2"/><path d="M55 48v16M47 56h16" stroke="#333" stroke-width="4"/></svg>
  </div>
  <p class="abs svc-name" style="left:176px;top:1873px">ELECTRONIC HEALTH RECORD<br>(EHR) SERVICES</p>
  <p class="abs svc-text" style="left:176px;top:1923px">Sed ut perspiciatis unde omnis iste natus error sit voluptatem accusan tium do loremque laudantium, totam rem aperiam, eaque ipsa quae ab illo inven tore veritatis et quasi architecto bea</p>
  <div class="abs btn-outline" style="left:268px;top:2073px;width:176px;height:50px">More Information</div>

  <div class="abs svc-icon" style="left:778px;top:1739px">
    <svg width="107" height="107" viewBox="0 0 112 112"><circle cx="56" cy="38" r="9" fill="#333"/><path d="M40 62c0-8 7-12 16-12s16 4 16 12z" fill="#333"/><rect x="40" y="60" width="32" height="18" fill="#333"/><rect x="30" y="78" width="52" height="5" fill="#333"/></svg>
  </div>
  <p class="abs svc-name" style="left:655px;top:1873px">INFORMATION TECHNOLOGY<br>SERVICES</p>
  <p class="abs svc-text" style="left:655px;top:1923px">Sed ut perspiciatis unde omnis iste natus error sit voluptatem accusan tium do loremque laudantium, totam rem aperiam, eaque ipsa quae ab illo inven tore veritatis et quasi architecto bea</p>
  <div class="abs btn-outline" style="left:747px;top:2073px;width:176px;height:50px">More Information</div>
</section>

<section>
  <div class="abs contact"></div>
  <h2 class="abs contact-title">CONTACT</h2>
  <p class="abs hours-label">Opening Hours</p>
  <div class="abs hours-rule"></div>
  <div class="abs hours">
    <div><span>Monday-Saturday</span>: &nbsp;9am to 7pm</div>
    <div><span>Sunday</span>: &nbsp;Closed</div>
  </div>

  <div class="abs c-icon" style="left:157px;top:2400px">
    <svg width="14" height="16" viewBox="0 0 14 16"><path d="M7 1a5 5 0 0 1 5 5c0 4-5 9-5 9S2 10 2 6a5 5 0 0 1 5-5z" fill="none" stroke="#fff" stroke-width="1.6"/><circle cx="7" cy="6" r="1.8" fill="#fff"/></svg>
  </div>
  <p class="abs c-text" style="left:201px;top:2398px;width:200px">Carewell healthcare solutions, Brightvale (Northmere, Eastbrook), USA.</p>
  <div class="abs c-divider"></div>
  <div class="abs c-icon" style="left:440px;top:2400px">
    <svg width="14" height="14" viewBox="0 0 14 14"><path d="M3 1l2.5 3-1.5 1.5c.8 1.8 2.2 3.2 4 4L9.5 8 13 10.5 11.5 13C6 13 1 8 1 2.5z" fill="#fff"/></svg>
  </div>
  <p class="abs c-text" style="left:485px;top:2404px">555 - 014 - 7390</p>
  <div class="abs c-icon" style="left:440px;top:2462px">
    <svg width="14" height="12" viewBox="0 0 14 12"><rect x="0.8" y="0.8" width="12.4" height="10.4" fill="none" stroke="#fff" stroke-width="1.4"/><path d="M1 1l6 5 6-5" fill="none" stroke="#fff" stroke-width="1.4"/></svg>
  </div>
  <p class="abs c-text" style="left:485px;top:2466px">info@carewellhs.example</p>

  <div class="abs field" style="left:720px;top:2274px;width:154px">First Name</div>
  <div class="abs field" style="left:880px;top:2274px;width:154px">Last Name</div>
  <div class="abs field" style="left:720px;top:2318px;width:154px">Phone Number</div>
  <div class="abs field" style="left:880px;top:2318px;width:154px">Email Address</div>
  <div class="abs field area" style="left:720px;top:2360px;width:314px;height:85px">Your Message</div>
  <div class="abs send">Send Now</div>
</section>

<section>
  <div class="abs map" role="img" aria-label="Street map showing the office location"></div>
  <div class="abs map-btn">View Large Map</div>
</section>

<footer class="abs footer">Copyright 2018 &nbsp;All Rights Reserved.</footer>

</body>
</html>
```